Webdesign für freie Trauungen
Zielgruppe
Webseite für Hochzeitspaare, Trauerende, Bestatter, Interessierte
Aufgabenstellung
Internetseite
Briefing:
Onepager
Internetseite soll wirken:
Modern
Schlank
Klar
Vertrauenserweckend
professionell
Home:
Reden für besondere Momente im Leben
Schrift an Flyer anpassen
REDEN.
ERZÄHLEN.
ERINNERN.
BERÜHREN.
Bild von mir,
Dazu, meine Reden sind:
freundlich
authentisch
ehrlich
einfühlsam
taktvoll
humorvoll
tiefsinnig
tröstend
nett
zugewandt
interessant
nach Euren Wünschen
mit Euren Inhalten
individuell
sehr persönlich
kreativ
wortgewandt
erfahren
Sprechen Sie mich an! ?
FREIE TRAUUNG:
EINFACH HIMMLISCH!
eine Liebesgeschichte erzählen
Sich ein Versprechen geben
JA zueinander sagen
Mit lieben Menschen feiern
wo, wann, wie - das entscheidet Ihr!
Segensfeier - Willkommensfeier:
im Leben willkommen heißen
Was bedeutet der Name des Kindes?
Was wollt Ihr Eurem Kind mitgeben?
Was wünscht Ihr Euch für Euer Kind?
TRAUERFEIER:
an schöne Momente erinnern
Einen Menschen mit Worten lebendig werden lassen
Mit einer persönlichen und bewegenden Ansprache
Mit all dem, was Sie sich wünschen!
REDEN ZU GEBURTSTAGEN:
mit Humor, Witz und Verstand gemeinsam zurück schauen
Und von Träumen und Sehnsüchten erzählen
Reden zum Jubiläum:
gemeinsam zurück schauen
Geleistetes würdigen
Veränderungen verständlich machen
Ausblicke wagen
Biographien:
festhalten, damit nichts von Ihrer Lebensgeschichte verloren geht
Sie erinnern sich und ich schreibe auf
Referenzen:
???? Wie am besten ???
Persönliches Vita:
Studium an der Offenen Hochschule Berlin:
- Publizistik
Germanistik
Volkswirtschaftslehre
Lateinamerikanistik
Abschluß: Magistra Artium
Freie Rednerin seit 1998
Telefonnummer 015239870461
Email: doris.Kellmeyer@postfeld.de
Wirk..

```html
<!DOCTYPE html>
<html lang="de">
<head>
<meta charset="utf-8">
<title>Kellmeyer Reden</title>
<link rel="stylesheet" href="https://fonts.googleapis.com/css2?family=Source+Sans+3:ital,wght@0,300;0,400;0,600;1,300;1,400;1,600&display=swap">
<style>
:root{
  --teal:#5f8f8c;
  --teal-btn:#6b9794;
  --ink:#3e3e3e;
  --muted:#6d6d6d;
  --soft:#f1f2f0;
  --white:#ffffff;
  --footer:#333333;
}
*{box-sizing:border-box;margin:0;padding:0}
html,body{width:1200px;height:4874px;overflow:hidden}
body{font-family:"Source Sans 3",sans-serif;color:var(--ink);background:var(--white);position:relative}
.abs{position:absolute}

/* header */
.site-header{position:absolute;top:0;left:0;width:1200px;height:85px;background:var(--white)}
.brand{position:absolute;left:56px;top:20px;display:flex;align-items:center;gap:10px;font-size:28px;font-weight:300;color:var(--ink);letter-spacing:1px}
.brand .dot{width:10px;height:10px;border-radius:50%;background:var(--teal)}
.main-nav{position:absolute;top:36px;font-size:11px;letter-spacing:.3px;color:var(--ink);text-transform:uppercase}
.main-nav.active{color:var(--teal)}

/* hero */
.hero{position:absolute;top:85px;left:0;width:1200px;height:502px;background:var(--soft)}
.hero-photo{position:absolute;left:450px;top:0;width:750px;height:502px;background:linear-gradient(90deg,#8a9492 0%,#c9cdca 30%,#a4aba9 52%,#d8d4cc 70%,#6f7674 100%)}
.hero-title{position:absolute;left:136px;top:122px;font-size:37px;font-weight:300;line-height:44px;letter-spacing:1px}
.hero-sub{position:absolute;left:136px;top:334px;font-size:16px;line-height:20px;color:var(--teal);letter-spacing:.3px}

/* reden */
.portrait-circle{position:absolute;left:125px;top:712px;width:386px;height:386px;border-radius:50%;background:radial-gradient(circle at 50% 45%,#9a938a 0%,#b7c9c6 55%,#c2d6d4 100%);box-shadow:0 0 12px rgba(0,0,0,.15)}
.section-title{position:absolute;font-size:26px;font-weight:300;letter-spacing:1px;color:var(--ink)}
.cloud span{position:absolute;white-space:nowrap;color:#555;line-height:1}
.cloud .it{font-style:italic}
.cloud .b{font-weight:600}
.cloud .v{writing-mode:vertical-rl;transform:rotate(180deg)}
.btn{position:absolute;background:var(--teal-btn);color:var(--white);font-size:10px;font-weight:600;letter-spacing:.5px;display:flex;align-items:center;justify-content:center;text-transform:uppercase}

/* offers */
.offers{position:absolute;top:1202px;left:0;width:1200px;height:2385px;background:var(--soft)}
.offer-card{position:absolute;left:134px;width:930px;height:312px;background:var(--white);box-shadow:0 2px 10px rgba(0,0,0,.08)}
.offer-img{position:absolute;left:42px;top:38px;width:356px;height:237px}
.offer-title{position:absolute;left:464px;top:56px;font-size:20px;line-height:28px;color:var(--teal);letter-spacing:.5px;font-weight:400}
.offer-text{position:absolute;left:464px;font-size:16px;line-height:21px;color:#555;font-weight:300}
.quote-badge{position:absolute;left:856px;top:-11px;width:32px;height:30px;background:var(--teal-btn);display:flex;align-items:center;justify-content:center}

/* vita */
.vita-h{position:absolute;font-size:16px;line-height:20px;color:var(--teal);letter-spacing:.3px}
.vita-list{position:absolute;left:136px;top:3802px;font-size:11px;line-height:18px;color:var(--muted);list-style:none}
.vita-list li::before{content:"";display:inline-block;width:5px;height:5px;border-radius:50%;background:var(--muted);margin:0 10px 2px 4px}
.contact-box{position:absolute;left:386px;top:3748px;width:222px;height:284px;background:var(--soft)}
.contact-box .label{position:absolute;left:36px;top:86px;font-size:16px;color:var(--teal)}
.contact-box .line{position:absolute;left:36px;font-size:11px;color:var(--ink)}
.vita-photo{position:absolute;left:636px;top:3748px;width:428px;height:284px;background:linear-gradient(90deg,#2d5a52 0%,#557a70 40%,#cfc8bc 70%,#e3ddd2 100%)}

/* references */
.references{position:absolute;top:4146px;left:0;width:1200px;height:672px;background:radial-gradient(ellipse at 30% 60%,#dfe2e1 0%,#eceeed 45%,#e4e7e6 100%)}
.ref-back{position:absolute;left:360px;top:4356px;width:510px;height:360px;background:#c9d6d4;transform:rotate(-3deg)}
.ref-card{position:absolute;left:331px;top:4331px;width:521px;height:367px;background:var(--white);box-shadow:0 2px 14px rgba(0,0,0,.12)}
.ref-text{position:absolute;left:57px;top:58px;width:410px;font-size:13px;line-height:20px;color:#555;font-weight:300}
.ref-sign{position:absolute;left:57px;top:230px;font-size:13px;font-weight:600;color:#444}
.ref-arrow{position:absolute;top:4502px;width:30px;height:30px;background:var(--teal-btn);display:flex;align-items:center;justify-content:center}

/* footer */
.site-footer{position:absolute;top:4818px;left:0;width:1200px;height:56px;background:var(--footer);color:#eee}
.site-footer .brand{left:56px;top:12px;font-size:20px;color:#eee}
.site-footer .fl{position:absolute;top:22px;font-size:10px;letter-spacing:.3px}
</style>
</head>
<body>

<header class="site-header">
  <div class="brand"><span class="dot"></span>Kellmeyer</div>
  <nav>
    <span class="main-nav active" style="left:653px">Start</span>
    <span class="main-nav" style="left:719px">Meine Reden</span>
    <span class="main-nav" style="left:820px">Was ich anbiete</span>
    <span class="main-nav" style="left:941px">Persönliches Vita</span>
    <span class="main-nav" style="left:1073px">Referenzen</span>
  </nav>
</header>

<section class="hero">
  <h1 class="hero-title">REDEN.<br>ERZÄHLEN.<br>ERINNERN.<br>BERÜHREN.</h1>
  <p class="hero-sub">REDEN FÜR BESONDERE<br>MOMENTE IM LEBEN</p>
  <div class="hero-photo" role="img" aria-label="Foto der Rednerin, an eine Glasfassade gelehnt und gespiegelt"></div>
</section>

<section class="meine-reden">
  <div class="portrait-circle" role="img" aria-label="Porträtfoto der Rednerin im grauen Blazer"></div>
  <h2 class="section-title" style="left:711px;top:700px">MEINE REDEN SIND</h2>
  <div class="cloud">
    <span class="it b" style="left:770px;top:798px;font-size:13px">taktvoll</span>
    <span style="left:848px;top:798px;font-size:13px">interessant</span>
    <span class="v" style="left:610px;top:833px;font-size:18px">kreativ</span>
    <span class="v" style="left:642px;top:808px;font-size:11px">wortgewandt</span>
    <span class="b" style="left:681px;top:829px;font-size:26px">authentisch</span>
    <span style="left:844px;top:831px;font-size:22px">erfahren</span>
    <span class="it" style="left:956px;top:836px;font-size:18px">tiefsinnig</span>
    <span style="left:680px;top:883px;font-size:13px">nett</span>
    <span style="left:746px;top:873px;font-size:21px">einfühlsam</span>
    <span class="it b" style="left:897px;top:869px;font-size:26px">humorvoll</span>
    <span class="v" style="left:1038px;top:871px;font-size:17px">freundlich</span>
    <span class="it b" style="left:591px;top:917px;font-size:21px">zugewandt</span>
    <span style="left:725px;top:912px;font-size:27px">nach Euren Wünschen</span>
    <span class="v it b" style="left:1074px;top:918px;font-size:15px">tröstend</span>
    <span class="it" style="left:685px;top:960px;font-size:21px">sehrpersönlich</span>
    <span class="b" style="left:875px;top:960px;font-size:20px">mit Euren Inhalten</span>
    <span class="b" style="left:716px;top:1002px;font-size:14px">ehrlich</span>
    <span style="left:810px;top:1002px;font-size:14px">individuell</span>
  </div>
  <div class="btn" style="left:751px;top:1067px;width:167px;height:29px">Sprechen Sie mich an!</div>
</section>

<section class="offers">
  <h2 class="section-title" style="left:0;width:1200px;text-align:center;top:82px">WAS ICH ANBIETE</h2>
</section>

<svg width="0" height="0" style="position:absolute">
  <symbol id="quote" viewBox="0 0 16 12"><path d="M0 6h4l-2 5h3l2-5V0H0zM9 6h4l-2 5h3l2-5V0H9z" fill="#fff"/></symbol>
  <symbol id="chev" viewBox="0 0 10 10"><path d="M6.5 1.5 3 5l3.5 3.5" fill="none" stroke="#fff" stroke-width="1.4"/></symbol>
</svg>

<article class="offer-card" style="top:1395px">
  <div class="quote-badge"><svg width="14" height="11"><use href="#quote"/></svg></div>
  <div class="offer-img" role="img" aria-label="Foto eines Brautpaars beim Auszug mit Konfetti" style="background:linear-gradient(120deg,#3a3530,#8b8478 45%,#e6e2dc 75%,#b9b2a7)"></div>
  <h3 class="offer-title">FREIE TRAUUNG:<br>EINFACH HIMMLISCH!</h3>
  <p class="offer-text" style="top:134px">eine Liebesgeschichte erzählen<br>Sich ein Versprechen geben<br>JA zueinander sagen<br>Mit lieben Menschen feiern<br><br>wo, wann, wie – das entscheidet Ihr!</p>
</article>

<article class="offer-card" style="top:1753px">
  <div class="quote-badge"><svg width="14" height="11"><use href="#quote"/></svg></div>
  <div class="offer-img" role="img" aria-label="Foto einer Mutter mit lachendem Baby" style="background:linear-gradient(110deg,#6e5a46,#a58c72 40%,#dcd2c6 70%,#efe9e1)"></div>
  <h3 class="offer-title">SEGENSFEIER<br>WILLKOMMENSFEIER</h3>
  <p class="offer-text" style="top:134px">im Leben willkommen heißen<br>Was bedeutet der Name des Kindes?<br>Was wollt Ihr Eurem Kind mitgeben?<br>Was wünscht Ihr Euch für Euer Kind?</p>
</article>

<article class="offer-card" style="top:2111px">
  <div class="quote-badge"><svg width="14" height="11"><use href="#quote"/></svg></div>
  <div class="offer-img" role="img" aria-label="Foto eines weißen Blumenstraußes mit brennender Kerze" style="background:radial-gradient(ellipse at 40% 35%,#d8d6d8 0%,#6a6470 35%,#1e1c22 75%)"></div>
  <h3 class="offer-title">TRAUERFEIER</h3>
  <p class="offer-text" style="top:106px">an schöne Momente erinnern<br>Einen Menschen mit Worten<br>lebendig werden lassen<br>Mit einer persönlichen und<br>bewegenden Ansprache<br><br>Mit all dem, was Sie sich wünschen!</p>
</article>

<article class="offer-card" style="top:2469px">
  <div class="quote-badge"><svg width="14" height="11"><use href="#quote"/></svg></div>
  <div class="offer-img" role="img" aria-label="Foto einer Geburtstagsfeier im Garten" style="background:linear-gradient(160deg,#7c8a5c,#b3a98a 45%,#8a8675 70%,#5d6448)"></div>
  <h3 class="offer-title">REDEN ZU GEBURTSTAGEN</h3>
  <p class="offer-text" style="top:106px">mit Humor, Witz und Verstand<br>gemeinsam zurück schauen<br>Und von Träumen und Sehnsüchten<br>erzählen</p>
</article>

<article class="offer-card" style="top:2827px">
  <div class="quote-badge"><svg width="14" height="11"><use href="#quote"/></svg></div>
  <div class="offer-img" role="img" aria-label="Foto einer feiernden Gruppe beim Anstoßen" style="background:linear-gradient(130deg,#2f3b44,#7b8087 40%,#c9c4bd 65%,#4c5a63)"></div>
  <h3 class="offer-title">REDEN ZUM JUBILÄUM</h3>
  <p class="offer-text" style="top:106px">gemeinsam zurück schauen<br>Geleistetes würdigen<br>Veränderungen verständlich machen<br>Ausblicke wagen</p>
</article>

<article class="offer-card" style="top:3185px">
  <div class="quote-badge"><svg width="14" height="11"><use href="#quote"/></svg></div>
  <div class="offer-img" role="img" aria-label="Foto einer alten Schreibmaschine auf Holztisch" style="background:linear-gradient(120deg,#6b4a30,#9a7352 45%,#5a3d28 80%)"></div>
  <h3 class="offer-title">BIOGRAPHIEN</h3>
  <p class="offer-text" style="top:106px">festhalten, damit nichts von Ihrer<br>Lebensgeschichte verloren geht<br>Sie erinnern sich und ich schreibe auf</p>
</article>

<section class="vita">
  <h2 class="section-title" style="left:136px;top:3652px">PERSÖNLICHES VITA</h2>
  <h3 class="vita-h" style="left:136px;top:3750px">STUDIUM AN DER OFFENEN<br>HOCHSCHULE BERLIN</h3>
  <ul class="vita-list">
    <li>Publizistik</li><li>Germanistik</li><li>Volkswirtschaftslehre</li><li>Lateinamerikanistik</li><li>Abschluß: Magistra Artium</li>
  </ul>
  <h3 class="vita-h" style="left:136px;top:3914px">FREIE REDNERIN SEIT 1998</h3>
  <h3 class="vita-h" style="left:136px;top:3966px">WIRKUNGSKREIS</h3>
  <p class="abs" style="left:136px;top:3990px;font-size:11px;line-height:18px;color:var(--muted)">Aachen, Viersen, Düsseldorf,<br>Krefeld, Erkelenz, Neuss, Köln</p>
  <div class="contact-box">
    <span class="label">KONTAKT</span>
    <span class="line" style="top:128px">doris.kellmeyer@postfeld.de</span>
    <span class="line" style="top:155px">0152-39870461</span>
    <span class="line" style="top:182px;color:var(--teal)">kellmeyerreden.de</span>
  </div>
  <div class="vita-photo" role="img" aria-label="Porträtfoto der Rednerin mit Brille auf grünem Sessel"></div>
  <div class="btn" style="left:897px;top:4057px;width:167px;height:28px">Sprechen Sie mich an!</div>
</section>

<section class="references" role="img" aria-label="Hintergrund mit sanften Wasserringen"></section>
<h2 class="section-title" style="left:333px;top:4220px">REFERENZEN</h2>
<div class="ref-back"></div>
<div class="ref-card">
  <p class="ref-text">Hallo Doris,<br>wir möchten nur noch mal kurz "Danke" sagen für die tolle Zeremonie zu unserer Hochzeitsfeier! Es hat allen wunderbar gefallen. Besonderen Dank für Deine (Eure) Flexibilität, die der Regenschauer Euch "abgenötigt" hat! Chapeau! Wir wünschen Dir nur das Allerbeste! Anbei eine Danksagung als Erinnerung. Viele liebe Grüße.</p>
  <p class="ref-sign">Lena + Jonas</p>
</div>
<div class="ref-arrow" style="left:250px"><svg width="12" height="12"><use href="#chev"/></svg></div>
<div class="ref-arrow" style="left:918px"><svg width="12" height="12" style="transform:rotate(180deg)"><use href="#chev"/></svg></div>

<footer class="site-footer">
  <div class="brand"><span class="dot"></span>Kellmeyer</div>
  <span class="fl" style="left:441px">STARTSEITE</span>
  <span class="fl" style="left:526px">KONTAKT</span>
  <span class="fl" style="left:602px">IMPRESSUM</span>
  <span class="fl" style="left:687px">DATENSCHUTZ</span>
  <span class="fl" style="right:60px">COPYRIGHT @2021 DORIS KELLMEYER</span>
</footer>

</body>
</html>
```